Etiketten-Design für Weißwein
Zielgruppe
Wir betreiben einen Weingroßhandel, beliefern die Gastronomie mit Wein und haben einen Onlineshop unter kerstel-wein.de
Zielgruppe für diesen Wein: Gastronomie und Privatkunden, Altersgruppe: 25-40, Charakteristiken: jung, aufgeschlossen und lebenslustig.
Aufgabenstellung
Zum Produkt: Flaschenform Bordeauxflasche, Inhalt Weißwein feinherb und wertig von einem Top Weingut, als Sommerwein gedacht.
Das Etikett soll modern sein und auffallen. Unsere erste Idee war MIRAVELLO mit einem Spruch: Kein Ziel, kein Plan, aber fantastischen Wein. Wir freuen uns aber auch über neue Ideen.
u.U. könnten weitere Weine mit diesem Etikett mit leichten Anpassungen entstehen (z.B. ein Rotwein und ein Rose)

```html
<!DOCTYPE html>
<html lang="de">
<head>
<meta charset="utf-8">
<title>Miravello – Weißwein Etikett</title>
<link rel="stylesheet" href="https://fonts.googleapis.com/css2?family=Fira+Sans+Condensed:wght@400;500;600&display=swap">
<style>
  :root {
    --page: #ffffff;
    --label: #dcd7d1;
    --band: #8b857c;
    --line-light: #f4f2ef;
    --ink: #111111;
    --edge: #9a9690;
  }
  * { margin: 0; padding: 0; box-sizing: border-box; }
  html, body {
    width: 1200px;
    height: 1200px;
    overflow: hidden;
    background: var(--page);
  }
  .canvas {
    position: relative;
    width: 1200px;
    height: 1200px;
  }
  .label {
    position: absolute;
    left: 80px;
    top: 80px;
    width: 1040px;
    height: 1040px;
    background: var(--label);
    border: 1.5px solid var(--edge);
    font-family: "Fira Sans Condensed", sans-serif;
    color: var(--ink);
    text-align: center;
  }
  .label__top-rule {
    position: absolute;
    left: 0; right: 0;
    top: 114px;
    height: 4px;
    background: var(--line-light);
  }
  .label__band {
    position: absolute;
    left: 0; right: 0;
    top: 122px;
    height: 222px;
    background: var(--band);
    display: flex;
    align-items: center;
    justify-content: center;
  }
  .label__band-rule {
    position: absolute;
    left: 0; right: 0;
    top: 346px;
    height: 4px;
    background: var(--line-light);
  }
  .brand-name {
    font-family: "Fira Sans Condensed", sans-serif;
    font-weight: 400;
    font-size: 112px;
    letter-spacing: 6px;
    color: var(--line-light);
    line-height: 1;
  }
  .tagline {
    position: absolute;
    left: 0; right: 0;
    top: 442px;
    font-weight: 600;
    font-size: 62px;
    line-height: 85px;
    letter-spacing: 2px;
    text-transform: uppercase;
  }
  .label__divider {
    position: absolute;
    left: 152px;
    right: 152px;
    top: 705px;
    height: 4px;
    background: var(--ink);
  }
  .wine-info {
    position: absolute;
    left: 0; right: 0;
    top: 812px;
    font-weight: 400;
    font-size: 48px;
    line-height: 68px;
    letter-spacing: 2px;
  }
</style>
</head>
<body>
  <main class="canvas">
    <section class="label" aria-label="Weinetikett Miravello">
      <div class="label__top-rule"></div>
      <div class="label__band">
        <span class="brand-name">miravello</span>
      </div>
      <div class="label__band-rule"></div>
      <p class="tagline">Kein Ziel, kein Plan,<br>aber fantastischen Wein</p>
      <div class="label__divider"></div>
      <p class="wine-info">WEISSWEIN – FEINHERB<br>2020</p>
    </section>
  </main>
</body>
</html>
```